Australian home builder requires inclusion list design

We require two inclusions list's flyers to showcase our two different inclusions. The design of the flyer is to reinforce professionalism and quality.
One inclusions list for each specification (i.e Orin and Cornerway)

Target Market(s)

Home Buyers aged 25 - 55

Industry/Entity Type

Home Builder

Other font styles liked:
• Harabara

```html
<!DOCTYPE html>
<html lang="en">
<head>
<meta charset="utf-8">
<title>Cornerway Inclusions</title>
<link rel="stylesheet" href="https://fonts.googleapis.com/css2?family=Montserrat:wght@300;500;700&family=Open+Sans:ital,wght@0,400;1,400&display=swap">
<style>
:root{
  --green:#2fa84a;
  --green-dark:#1d7a33;
  --ink:#1f1f1f;
  --text:#3a3a3a;
  --band:#efefef;
  --backdrop:#2b2b2b;
  --page:#ffffff;
}
*{box-sizing:border-box;margin:0;padding:0}
html,body{width:1200px;height:845px;overflow:hidden;background:var(--backdrop)}
.page{position:absolute;top:65px;width:529px;height:748px;background:var(--page);overflow:hidden}
.page--front{left:38px}
.page--back{left:631px}
.header-band,.footer-band{position:absolute;left:0;width:529px}
.header-band{top:0;height:80px}
.footer-band{bottom:0;height:80px}
.title{position:absolute;top:14px;left:0;width:100%;text-align:center;font-family:'Montserrat',sans-serif;font-size:31px;letter-spacing:.5px;color:#444}
.title strong{color:var(--green);font-weight:700}
.title span{font-weight:300}
.brand{display:flex;align-items:center;gap:6px;font-family:'Montserrat',sans-serif;font-weight:700;color:var(--green)}
.brand-mark{background:var(--green);display:block}
.brand--head{position:absolute;top:18px;left:0;width:100%;justify-content:center;font-size:21px}
.brand--head .brand-mark{width:24px;height:24px}
.brand--foot{position:absolute;right:28px;bottom:24px;font-size:14px}
.brand--foot .brand-mark{width:16px;height:16px}
.col{position:absolute;top:110px;width:235px;font-family:'Open Sans',sans-serif}
.col--a{left:26px}
.col--b{left:272px}
.section{font-family:'Montserrat',sans-serif;font-weight:700;color:var(--green);font-size:10.5px;line-height:1.2;margin:7px 0 4px;text-transform:uppercase}
.col>.section:first-child{margin-top:0}
.item{margin-bottom:3.6px}
.item h3{font-family:'Montserrat',sans-serif;font-weight:500;font-size:8px;color:var(--ink);line-height:1.15;text-transform:uppercase}
.item ul{list-style:none}
.item li{font-size:6px;line-height:1.38;color:var(--text);padding-left:8px;position:relative}
.item li::before{content:"•";position:absolute;left:1px}
.item em{font-style:italic}
.note{font-size:5.3px;font-style:italic;color:var(--text);margin:-3px 0 4px}
.two-up{display:flex;gap:12px}
.contact-front{position:absolute;left:26px;bottom:22px;width:250px;display:grid;grid-template-columns:1fr 80px;row-gap:3px;font-family:'Open Sans',sans-serif;font-size:6px;color:var(--text)}
.contact-back{position:absolute;left:26px;right:20px;bottom:26px;display:flex;justify-content:space-between;align-items:center;font-family:'Open Sans',sans-serif;font-size:6.3px;color:var(--text)}
.c{display:flex;align-items:center;gap:4px}
.ic{flex:none}
.sq{display:block;background:var(--green);border-radius:1px}
</style>
</head>
<body>

<section class="page page--front">
  <svg class="header-band" viewBox="0 0 529 80" aria-hidden="true">
    <polygon points="0,0 529,0 529,50 264.5,70 0,50" fill="var(--band)"/>
    <polygon points="0,50 264.5,70 529,50 529,55 264.5,75 0,55" fill="var(--green)"/>
    <polygon points="0,55 264.5,75 529,55 529,58 264.5,78 0,58" fill="var(--green-dark)"/>
  </svg>
  <h1 class="title"><strong>CORNERWAY</strong> <span>INCLUSIONS</span></h1>

  <div class="col col--a">
    <h2 class="section">External Feature</h2>
    <div class="item"><h3>External Wall Constructions</h3><ul><li>Smooth Cement rendered block construction</li></ul></div>
    <div class="item"><h3>Metal Roofing</h3><ul><li>Ferrocoat custom orb roofing from the standard Ferrocoat range.</li></ul></div>
    <div class="item"><h3>Fascia &amp; Gutter</h3><ul><li>Ferrocoat fascia and gutter from the standard Ferrocoat range</li></ul></div>
    <div class="item"><h3>Windows</h3><ul><li>Powdercoat Aluminium windows and doors</li></ul></div>
    <div class="item"><h3>Window Screens</h3><ul><li>Flyscreens to all aluminium windows and doors</li></ul></div>
    <div class="item"><h3>Entrance Doors</h3><ul><li>Selection of Harlow Doors from the Brightwell Homes Cornerway Range</li></ul></div>
    <div class="item"><h3>Entrance Door Furniture</h3><ul><li>Kingsgate Securelatch or Kingsgate K4 Series 450mm Oblong Pull Handle Entrance Set</li></ul></div>
    <div class="item"><h3>External Cladding</h3><ul><li>Lightweight cladding to outer walls where indicated <em>(refer design plans)</em></li></ul></div>
    <div class="item"><h3>Driveway</h3><ul><li>Exposed Aggregate driveway as shown on design plans</li></ul></div>
    <div class="item"><h3>Patio</h3><ul><li>Exposed Aggregate to the fascia line as indicated on design plans</li></ul></div>
    <div class="item"><h3>Clothesline</h3><ul><li>Wallfold wall hung clothesline</li><li>Exposed Aggregate Drying Court as per design plans</li></ul></div>
    <div class="item"><h3>Mailbox</h3><ul><li>Choice of Mailbox from Brightwell Homes Cornerway Range</li></ul></div>

    <h2 class="section">Site-Specific Costs</h2>
    <div class="item"><h3>Site Survey</h3><ul><li>Soil Testing, Wind Classification and Contour Plan</li></ul></div>
    <div class="item"><h3>Site Levels</h3><ul><li>Site Cut/Fill, maximum of 400mm and 400mm fill</li></ul></div>
    <div class="item"><h3>Sanitary Services</h3><ul><li>Storm Water, Sewer, and water connections as per Westbrook Regional Council Requirements</li></ul></div>
    <div class="item"><h3>Utility Connections</h3><ul><li>Power connections to Northgrid requirements and FibreNet Lead in Cabling</li></ul></div>

    <h2 class="section">Kitchen</h2>
    <div class="item"><h3>Oven</h3><ul><li>Velden Multifunction Stainless Steel Oven</li></ul></div>
    <div class="item"><h3>Cooktop</h3><ul><li>Velden 60cm Ceramic Cooktop</li></ul></div>
    <div class="item"><h3>Rangehood</h3><ul><li>Velden 60cm slide-out rangehood</li></ul></div>
    <div class="item"><h3>Sink</h3><ul><li>Ravelle Essential 1 ¾ Bowl Sink</li></ul></div>
    <div class="item"><h3>Sink Mixer</h3><ul><li>Ravelle Pivot Pin Lever</li></ul></div>
    <div class="item"><h3>Dishwasher</h3><ul><li>Velden Freestanding stainless look Dishwasher</li></ul></div>
  </div>

  <div class="col col--b">
    <div class="item"><h3>Splashback</h3><ul><li>Ceramic Tiles above all benchtop surfaces up to the top cupboard height</li></ul></div>
    <div class="item"><h3>Cabinetry</h3><ul><li>Lamitek Finish with the inclusion of 2 x Pot Draws and 1 x bank of cutlery draws.</li><li>Laminated Top cupboards <em>(refer to design plans)</em></li></ul></div>
    <div class="item"><h3>Benchtops</h3><ul><li>Choice of Square Edge or Bullnose Laminated Benchtops</li></ul></div>

    <h2 class="section">Floor Coverings</h2>
    <div class="item"><h3>Vinyl Plank</h3><ul><li>Vinyl Plank Flooring as indicated on design plans from Brightwell Homes Cornerway Range</li></ul></div>
    <div class="item"><h3>Carpet</h3><ul><li>Carpet as indicated on design plans from the Brightwell Homes Cornerway Range</li></ul></div>

    <h2 class="section">Tiling</h2>
    <div class="item"><h3>Floor and Wall Tiles</h3><ul><li>Ceramic Floor tiles to wet areas as indicated on design plans from the Bayside Tiles Silver Range</li><li>Ceramic Wall tiles to wet areas as indicated on design plans from the Bayside Tiles Silver Range (Kitchen, Laundry and Vanity Splashbacks: Shower Cubicles and Bath)</li><li>Skirting Tiles to all Wet areas</li></ul></div>

    <h2 class="section">Bathrooms, Ensuite and WC</h2>
    <div class="item"><h3>Vanity Unit</h3><ul><li>Laminated Finish with Laminated Square Edge or Bullnose Benchtop</li><li>One bank of draws</li></ul></div>
    <div class="item"><h3>Vanity Basin</h3><ul><li>Ravelle Langley Drop-In</li></ul></div>
    <div class="item"><h3>Basin Mixer</h3><ul><li>Ravelle Pivot Pin Lever</li></ul></div>
    <div class="item"><h3>Bath</h3><ul><li>Recline Bathtub 1650mm</li><li>Marina Freestanding Bathtub <em>(Plan Specific)</em></li></ul></div>
    <div class="item"><h3>Bath Mixer</h3><ul><li>Ravelle Pivot Pin Level</li><li>Ravelle Hale Bath Spout</li></ul></div>
    <div class="item"><h3>Shower Mixer</h3><ul><li>Ravelle Pivot Pin Lever</li></ul></div>
    <div class="item"><h3>Shower Head</h3><ul><li>Ravelle Alto 3 Function</li></ul></div>
    <div class="item"><h3>Shower Base</h3><ul><li>Tiled as per design plans</li></ul></div>
    <div class="item"><h3>Shower Screen</h3><ul><li>Clear laminated pivot screen <em>(Plan Specific)</em></li><li>Walk-in shower <em>(Plan specific)</em></li></ul></div>
    <div class="item"><h3>Toilet</h3><ul><li>Classic Toilet suite</li></ul></div>
    <div class="item"><h3>Towel Rail Holder</h3><ul><li>Ravelle Pivot Double Towel Rail</li></ul></div>
    <div class="item"><h3>Toilet Roll Holder</h3><ul><li>Ravelle Pivot Toilet roll holder</li></ul></div>
  </div>

  <svg class="footer-band" viewBox="0 0 529 80" aria-hidden="true">
    <polygon points="0,0 264.5,12 529,0 529,5 264.5,17 0,5" fill="var(--green)"/>
    <polygon points="0,5 264.5,17 529,5 529,8 264.5,20 0,8" fill="var(--green-dark)"/>
    <polygon points="0,10 264.5,22 529,10 529,80 0,80" fill="var(--band)"/>
  </svg>
  <div class="contact-front">
    <div class="c"><svg class="ic" width="7" height="8" viewBox="0 0 10 12"><path d="M5 0a4 4 0 0 0-4 4c0 3 4 8 4 8s4-5 4-8a4 4 0 0 0-4-4z" fill="var(--green)"/><circle cx="5" cy="4" r="1.5" fill="#fff"/></svg>24 Harbourview Road, Westbrook 4810</div>
    <div></div>
    <div class="c"><svg class="ic" width="7" height="7" viewBox="0 0 10 10"><path d="M2 0l2 2.5-1.2 1.3a6 6 0 0 0 3.4 3.4L7.5 6 10 8l-1.5 2C4 10 0 6 0 1.5z" fill="var(--green)"/></svg>(07) 4000 1234</div>
    <div class="c"><span class="sq" style="width:6px;height:6px"></span>brightwellhomes</div>
    <div class="c"><svg class="ic" width="7" height="7" viewBox="0 0 10 10"><circle cx="5" cy="5" r="4.3" fill="none" stroke="var(--green)" stroke-width="1.2"/><path d="M1 5h8M5 .7c-2.5 2.6-2.5 5.9 0 8.6M5 .7c2.5 2.6 2.5 5.9 0 8.6" stroke="var(--green)" fill="none" stroke-width=".9"/></svg>brightwellhomes.com.au</div>
    <div class="c"><span class="sq" style="width:6px;height:6px"></span>brightwellhomes</div>
  </div>
  <div class="brand brand--foot"><span class="brand-mark"></span>Brightwell Homes</div>
</section>

<section class="page page--back">
  <svg class="header-band" viewBox="0 0 529 80" aria-hidden="true">
    <polygon points="0,0 529,0 529,50 264.5,70 0,50" fill="var(--band)"/>
    <polygon points="0,50 264.5,70 529,50 529,55 264.5,75 0,55" fill="var(--green)"/>
    <polygon points="0,55 264.5,75 529,55 529,58 264.5,78 0,58" fill="var(--green-dark)"/>
  </svg>
  <div class="brand brand--head"><span class="brand-mark"></span>Brightwell Homes</div>

  <div class="col col--a">
    <h2 class="section">Laundry</h2>
    <div class="item"><h3>Laundry Tub</h3><ul><li>Kona laundry tub and cabinet</li></ul></div>
    <div class="item"><h3>Laundry Mixer</h3><ul><li>Ravelle Pivot Pin Lever</li></ul></div>
    <div class="item"><h3>Washing Machine Taps</h3><ul><li>Taps installed inside of laundry cupboard</li></ul></div>
    <div class="item"><h3>Splashback</h3><ul><li>600mm high splashback above benchtop and washing machine space from Bayside Tiles Silver Range</li></ul></div>

    <h2 class="section">Garage</h2>
    <div class="item"><h3>Garage Doors</h3><ul><li>Ferrocoat panel lift door with two remotes from standard Colour Range</li></ul></div>
    <div class="item"><h3>External Access Doors</h3><ul><li>Solid Core External Door <em>(Plan specific)</em></li></ul></div>

    <h2 class="section">Internal Features</h2>
    <div class="item"><h3>Ceiling Heights</h3><ul><li>2400mm</li></ul></div>
    <div class="item"><h3>Wall Linings</h3><ul><li>Plasterboard to wall linings and ceilings</li><li>Cemboard to Bathrooms and Ensuite</li></ul></div>
    <div class="item"><h3>Cornice</h3><ul><li>90mm Cove cornice</li></ul></div>
    <div class="item"><h3>Internal Doors</h3><ul><li>Harlow Flush Panel 2040mm high door</li></ul></div>
    <div class="item"><h3>Door Furniture</h3><ul><li>Kingsgate K4 Series</li></ul></div>
    <div class="item"><h3>Architraves</h3><ul><li>42mm x 12mm <em>(Selection available)</em></li></ul></div>
    <div class="item"><h3>Skirting</h3><ul><li>68 x 12mm <em>(Selection available)</em></li></ul></div>
    <div class="item"><h3>Windows Reveals</h3><ul><li>FJP Pine reveals</li></ul></div>

    <h2 class="section">Paintwork</h2>
    <div class="item"><h3>External</h3><ul><li>One colour to soffits and one colour to wall gloss acrylic plus one feature colour</li></ul></div>
    <div class="item"><h3>Internal Walls</h3><ul><li>Low sheen acrylic (3 coat system)</li></ul></div>
    <div class="item"><h3>Internal Ceilings</h3><ul><li>Ceiling Paint ( 3 coat system)</li></ul></div>
    <div class="item"><h3>Internal Woodwork and Doors</h3><ul><li>Semi-Gloss Finish to doors, architraves and skirtings</li></ul></div>

    <h2 class="section">Insulation</h2>
    <div class="item"><h3>Roof Insulation</h3><ul><li>60mm Loftguard Roof Blanket</li></ul></div>

    <h2 class="section">Hot Water System</h2>
    <div class="item"><ul><li>Thermo 250 Litre</li></ul></div>
  </div>

  <div class="col col--b" style="width:235px">
    <h2 class="section">Storage Cupboards</h2>
    <div class="item"><h3>Robes</h3><ul><li>Aluminium Sliding Mirrored/Vinyl doors with ShelfPro shelf and hanging rail</li></ul></div>
    <div class="item"><h3>Linen/Storage</h3><ul><li>Aluminium Sliding Vinyl Doors with ShelfPro four-shelf system</li></ul></div>
    <div class="item"><h3>Broom</h3><ul><li>Single ShelfPro shelf</li></ul></div>

    <h2 class="section">Electrical</h2>
    <p class="note">(refer individual design plan with the consultant)</p>
    <div class="item"><h3>Light Points</h3><ul><li>LED downlights</li></ul></div>
    <div class="item"><h3>Powerpoints</h3><ul><li>Voltra Classic series double power points (white throughout)</li><li>Voltra classic series single power pints to Fridge/rangehood/microwave/ Garage Door</li></ul></div>
    <div class="item"><h3>Smoke Alarms</h3><ul><li>Hardwired smoke alarms to comply with QLD smoke alarm legislation</li></ul></div>
    <div class="item"><h3>TV Point</h3><ul><li>Tv points located in living rooms/theatres/Master Bedrooms</li></ul></div>
    <div class="item"><h3>TV Antennae</h3><ul><li>Digital compliant tv antennae</li></ul></div>
    <div class="item"><h3>FibreNet</h3><ul><li>Distribution cabinet all internal data cables to terminate this point</li></ul></div>
    <div class="item"><h3>Safety Switches</h3><ul><li>Safety switches to meter box to comply with current QLD Electrical legislation</li></ul></div>

    <h2 class="section">Engineering</h2>
    <div class="item"><h3>Wind Rating</h3><ul><li>C2 Wind Category (AS2870)</li></ul></div>
    <div class="item"><h3>Concrete Slab</h3><ul><li>Engineer designed concrete slab to meet M Class foundation type (AS2870)</li></ul></div>
    <div class="item"><h3>Framing</h3><ul><li>Timber and concrete block framing as per design plans and engineer specifications</li></ul></div>
    <div class="item"><h3>Roof Trusses</h3><ul><li>Designed to Manufacturers specifications</li></ul></div>

    <h2 class="section">Termite Protection</h2>
    <div class="item"><h3>Framing</h3><ul><li>LOSP treated timber framing and roof trusses</li></ul></div>
    <div class="item"><h3>Mouldings</h3><ul><li>LOSP treated architraves/skirtings and door reveals</li></ul></div>
    <div class="item"><h3>Slab</h3><ul><li>Slab with penetration collars</li></ul></div>

    <h2 class="section">Preliminaries</h2>
    <div class="item two-up">
      <ul><li>Consulting Engineer</li><li>Building Design Plans</li><li>Surveyor Setout of Building</li><li>Construction Works Insurance</li></ul>
      <ul><li>Colour consultancy</li><li>SBCA Home owners warranty insurance</li><li>Building and Plumbing application fees</li><li>6-star minimum energy rating</li></ul>
    </div>
  </div>

  <svg class="footer-band" viewBox="0 0 529 80" aria-hidden="true">
    <polygon points="0,0 264.5,12 529,0 529,5 264.5,17 0,5" fill="var(--green)"/>
    <polygon points="0,5 264.5,17 529,5 529,8 264.5,20 0,8" fill="var(--green-dark)"/>
    <polygon points="0,10 264.5,22 529,10 529,80 0,80" fill="var(--band)"/>
  </svg>
  <div class="contact-back">
    <div class="c"><svg class="ic" width="11" height="13" viewBox="0 0 10 12"><path d="M5 0a4 4 0 0 0-4 4c0 3 4 8 4 8s4-5 4-8a4 4 0 0 0-4-4z" fill="var(--green)"/><circle cx="5" cy="4" r="1.5" fill="#fff"/></svg><span>24 Harbourview Road,<br>4810 Westbrook</span></div>
    <div class="c"><svg class="ic" width="11" height="11" viewBox="0 0 10 10"><path d="M2 0l2 2.5-1.2 1.3a6 6 0 0 0 3.4 3.4L7.5 6 10 8l-1.5 2C4 10 0 6 0 1.5z" fill="var(--green)"/></svg>(07) 4000 1234</div>
    <div class="c"><svg class="ic" width="11" height="11" viewBox="0 0 10 10"><circle cx="5" cy="5" r="4.3" fill="none" stroke="var(--green)" stroke-width="1.2"/><path d="M1 5h8M5 .7c-2.5 2.6-2.5 5.9 0 8.6M5 .7c2.5 2.6 2.5 5.9 0 8.6" stroke="var(--green)" fill="none" stroke-width=".9"/></svg>brightwellhomes.com.au</div>
    <div class="c"><span class="sq" style="width:10px;height:10px"></span>brightwellhomes</div>
    <div class="c"><span class="sq" style="width:10px;height:10px"></span>brightwellhomes</div>
  </div>
</section>

</body>
</html>
```